DOUBLE SIDED BROCHURE NEEDED TO PROMOTE DOCTOR

I need a double sided DL size (99mm x 210mm) brochure, promoting a doctor seeing patients in a new area.

I want something professional. I have included the relevant information. I would also like the Dr's picture somwhere in the brochure, with a professional background. I wish to print these tomorrow, so i will pick a winner within 14 hours of posting this ad.

I have included an example of a brochures design that I recently saw, and its definietly a good starting point.

Medical

```html
<!DOCTYPE html>
<html lang="en">
<head>
<meta charset="utf-8">
<title>Specialist Surgeon DL Brochure</title>
<link href="https://fonts.googleapis.com/css2?family=Ubuntu:wght@300;400;500;700&family=Oswald:wght@500;600&family=Open+Sans:wght@300;400&display=swap" rel="stylesheet">
<style>
  :root {
    --board: #3a0e1b;
    --label: #5b4a56;
    --red-top: #d8401a;
    --red-bottom: #e61f0a;
    --lime: #8ff000;
    --orange: #fb7a0c;
    --navy: #143a4d;
    --purple-top: #c567ec;
    --purple-bottom: #9850e4;
    --blush: #f3e8ef;
    --white: #ffffff;
    --muted: #e5d2f2;
  }
  * { margin: 0; padding: 0; box-sizing: border-box; }
  html, body { width: 1200px; height: 1200px; overflow: hidden; background: var(--board); }
  .board { position: relative; width: 1200px; height: 1200px; }
  .board-label {
    position: absolute; top: 12px; left: 0; width: 1200px; text-align: center;
    font: 400 38px/1 "Ubuntu", sans-serif; color: var(--label); letter-spacing: 1px;
  }
  .panel { position: absolute; top: 119px; width: 489px; height: 1035px; overflow: hidden; }
  .panel-front { left: 69px; }
  .panel-back { left: 634px; }
  .panel svg.bg { position: absolute; inset: 0; }
  .text { position: absolute; color: var(--white); font-family: "Ubuntu", sans-serif; }

  .greeting { left: 39px; top: 484px; font-size: 17.6px; font-weight: 700; }
  .announce { left: 39px; top: 522px; width: 420px; font-size: 17.6px; line-height: 23px; font-weight: 400; letter-spacing: 0.3px; }
  .announce p + p { margin-top: 23px; }

  .clinic-box {
    position: absolute; left: 78px; top: 758px; width: 336px; height: 119px;
    background: var(--navy); color: var(--white); text-align: center; font-family: "Ubuntu", sans-serif;
  }
  .clinic-name { margin-top: 6px; font-size: 25px; font-weight: 700; text-decoration: underline; text-decoration-thickness: 2px; text-underline-offset: 4px; }
  .clinic-address { margin-top: 12px; font-size: 19px; font-weight: 500; line-height: 31px; }

  .phone-band {
    position: absolute; left: 0; top: 894px; width: 489px; height: 63px; background: var(--orange);
    display: flex; align-items: center; color: var(--white);
  }
  .phone-band svg { margin-left: 32px; }
  .phone-number { margin-left: 22px; font: 500 41px/1 "Oswald", sans-serif; letter-spacing: -0.5px; transform: scaleY(1.05); }
  .fax-band {
    position: absolute; left: 0; top: 957px; width: 489px; height: 78px; background: var(--navy);
    color: var(--white); text-align: center;
  }
  .fax-label { margin-top: 6px; font: 300 18px/1.2 "Open Sans", sans-serif; }
  .fax-number { font: 700 33px/1.1 "Ubuntu", sans-serif; letter-spacing: 1px; }

  .back-title {
    position: absolute; left: 0; top: 0; width: 489px; height: 73px; background: var(--orange);
    color: var(--white); text-align: center; font: 600 38px/73px "Oswald", sans-serif; letter-spacing: -0.5px;
  }
  .intro { left: 54px; top: 436px; width: 420px; font-size: 20.5px; line-height: 25px; }
  .checklist { position: absolute; left: 92px; list-style: none; color: var(--white); font-family: "Ubuntu", sans-serif; font-size: 19.5px; }
  .checklist li { position: relative; padding-left: 22px; margin-bottom: 8px; line-height: 23px; }
  .checklist li::before {
    content: ""; position: absolute; left: 1px; top: 6px; width: 12px; height: 6px;
    border-left: 2px solid var(--white); border-bottom: 2px solid var(--white); transform: rotate(-45deg);
  }
  .checklist .note { display: block; color: var(--muted); font-size: 19px; line-height: 23px; }
  .list-specialist { top: 529px; }
  .general-heading { left: 60px; top: 734px; font-size: 20.5px; }
  .list-general { top: 773px; }
  .list-general li { margin-bottom: 9px; }
</style>
</head>
<body>
<div class="board">
  <div class="board-label">DESIGN IDEA - 01c</div>

  <!-- Front panel -->
  <section class="panel panel-front">
    <svg class="bg" width="489" height="1035" viewBox="0 0 489 1035">
      <defs>
        <linearGradient id="frontPhoto" x1="0" y1="0" x2="0" y2="1">
          <stop offset="0" stop-color="#6f9fd8"/>
          <stop offset="0.45" stop-color="#d9e4ef"/>
          <stop offset="1" stop-color="#4c5158"/>
        </linearGradient>
        <linearGradient id="frontBody" x1="0" y1="0" x2="0" y2="1">
          <stop offset="0" stop-color="var(--red-top)"/>
          <stop offset="1" stop-color="var(--red-bottom)"/>
        </linearGradient>
      </defs>
      <rect role="img" aria-label="Photo of the surgeon standing in front of a modern hospital building" x="0" y="0" width="489" height="470" fill="url(#frontPhoto)"/>
      <path d="M0 400 Q 245 520 489 390 L489 1035 L0 1035 Z" fill="var(--lime)"/>
      <path d="M0 428 Q 250 540 489 452 L489 1035 L0 1035 Z" fill="url(#frontBody)"/>
    </svg>

    <div class="text greeting">Dear Doctors,</div>
    <div class="text announce">
      <p>We are pleased to announce that Dr. Omar Halabi is now consulting in Coralbay, seeing public and private patients.</p>
      <p>Guaranteed appointment within two weeks, with patients having the option of surgery at Estuary Health Campus, Riverside General Hospital or St. Clare's Private Hospital.</p>
    </div>

    <div class="clinic-box">
      <div class="clinic-name">Coralbay Clinic</div>
      <div class="clinic-address">42 Seaview Road<br>Coralbay WA 6999.</div>
    </div>

    <div class="phone-band">
      <svg width="34" height="26" viewBox="0 0 34 26" aria-hidden="true">
        <path d="M2 9 Q17 -2 32 9 L30 13 L24 11 L24 7 Q17 4 10 7 L10 11 L4 13 Z" fill="var(--white)"/>
        <path d="M9 13 L25 13 L30 24 L4 24 Z" fill="var(--white)"/>
        <circle cx="17" cy="18" r="3" fill="var(--orange)"/>
      </svg>
      <span class="phone-number">PHONE - 1300 555 012</span>
    </div>
    <div class="fax-band">
      <div class="fax-label">Please send all referrals by fax to</div>
      <div class="fax-number">(08) 5550 0142</div>
    </div>
  </section>

  <!-- Back panel -->
  <section class="panel panel-back">
    <svg class="bg" width="489" height="1035" viewBox="0 0 489 1035">
      <defs>
        <linearGradient id="backBody" x1="0" y1="0" x2="0" y2="1">
          <stop offset="0" stop-color="var(--purple-top)"/>
          <stop offset="1" stop-color="var(--purple-bottom)"/>
        </linearGradient>
        <linearGradient id="portrait" x1="0" y1="0" x2="0" y2="1">
          <stop offset="0" stop-color="#b9d3ee"/>
          <stop offset="1" stop-color="#3b3f4a"/>
        </linearGradient>
      </defs>
      <rect x="0" y="73" width="489" height="962" fill="var(--blush)"/>
      <path d="M0 265 Q 245 345 489 265 L489 1035 L0 1035 Z" fill="url(#backBody)"/>
      <path d="M0 952 Q 245 1000 489 952 L489 1035 L0 1035 Z" fill="var(--white)"/>
      <path d="M0 960 Q 245 1008 489 960 L489 1035 L0 1035 Z" fill="var(--orange)"/>
      <circle cx="238" cy="247" r="162" fill="var(--white)"/>
      <circle role="img" aria-label="Portrait photo of the surgeon" cx="238" cy="247" r="151" fill="url(#portrait)"/>
    </svg>

    <h1 class="back-title">ABOUT DR. OMAR HALABI</h1>

    <div class="text intro">Dr. Halabi is a highly trained specialised surgeon, in all areas of Endocrine, Breast and General Surgery. Including;</div>
    <ul class="checklist list-specialist">
      <li>Thyroid Surgery</li>
      <li>Parathyroid surgery<span class="note">(including minimally invasive parathyroidectomy)</span></li>
      <li>Breast Cancer</li>
      <li>Benign breast lesions</li>
    </ul>

    <div class="text general-heading">All areas of general surgery, such as;</div>
    <ul class="checklist list-general">
      <li>Gallbladder surgery</li>
      <li>Hernia surgery</li>
      <li>Haemorrhoids</li>
      <li>Carpal Tunnel</li>
      <li>Vasectomy etc etc...</li>
    </ul>
  </section>
</div>
</body>
</html>
```